Social Action Network Needs Banner Ads for Cause T-Shirts

Hope in Hand is a social action network that transforms ordinary internet actions into donations to non-profit organizations fighting for a better tomorrow. Users can donate their social influence, print coupons, accept free offers or shop online and every action benefits causes they love. You can watch a video here: http://www.hopeinhand.example/

We are about to launch a line of cause tees that benefit the various causes we support. We want the banner ads to be positive, uplifting, inspiring and attractive. We want the ads to incorporate the following wording (although, we encourage creativity): Dress better so others can live better.

We require typical banner ad sizes: 300 x 250, 160 x 600, 728 x 90 (more sizes would be much appreciated).

Please try to include the Hope in Hand logo (color can be changed based on ad design).

In case it helps, here is a link to a page we have set up for one of our partner charities: http://www.hopeinhand.example/KindnessWells

Target Market(s)

While 80% of our users are women, we need to appeal to both.

Industry/Entity Type

Non-Profit

Requirements
Must have
• Hope in Hand logo and T-shirt design (with or without model). Also, some sort of call to action button - get tees, take action, buy now, check it out, learn more, etc.
Nice to have
• Feature the woman's tees and if possible the man's tees could be somewhere smaller in the background (if design allows).

```html
<!DOCTYPE html>
<html lang="en">
<head>
<meta charset="utf-8">
<title>Hope in Hand — Cause Tee Banner Set</title>
<link href="https://fonts.googleapis.com/css2?family=Bebas+Neue&family=Lato:wght@400&display=swap" rel="stylesheet">
<style>
  :root {
    --backdrop: #e2e2e2;
    --backdrop-light: #f4f4f4;
    --sun: #f8d312;
    --lime: #8dc63f;
    --leaf: #1ca55b;
    --olive: #a19d17;
    --white: #ffffff;
    --ink: #222222;
    --btn-top: #3b86cf;
    --btn-mid: #15569c;
    --btn-bottom: #0a2c5c;
    --tee-blue: #1e8fe0;
    --tee-blue-dark: #1467b0;
    --tee-grey: #4c4f52;
    --tee-grey-dark: #2f3133;
    --skin-bg: #e9c9a6;
  }
  * { margin: 0; padding: 0; box-sizing: border-box; }
  html, body { width: 1200px; height: 808px; overflow: hidden; }
  body {
    background: radial-gradient(ellipse at 45% 18%, var(--backdrop-light) 0%, var(--backdrop) 60%);
    font-family: "Bebas Neue", "Arial Narrow", sans-serif;
    position: relative;
  }
  .banner {
    position: absolute;
    overflow: hidden;
    border: 1px solid #333;
    box-shadow: 3px 4px 6px rgba(0,0,0,.35);
    background: linear-gradient(165deg, var(--sun) 0%, var(--lime) 45%, var(--leaf) 85%);
  }
  .banner > * { position: absolute; }
  .photo-woman {
    background: linear-gradient(180deg, #3a2a22 0%, var(--skin-bg) 28%, var(--tee-blue) 45%, var(--tee-blue-dark) 85%, #222 100%);
    border-radius: 40% 40% 6px 6px / 18% 18% 6px 6px;
  }
  .photo-man {
    background: linear-gradient(180deg, #2a2a2a 0%, var(--skin-bg) 25%, var(--tee-grey) 42%, var(--tee-grey-dark) 100%);
    border-radius: 40% 40% 6px 6px / 18% 18% 6px 6px;
  }
  .headline-box {
    background: var(--white);
    color: var(--olive);
    line-height: .92;
    padding: 2px 4px 0;
    white-space: nowrap;
  }
  .subline {
    color: var(--white);
    text-align: right;
    line-height: .9;
    white-space: nowrap;
    text-shadow: 1px 1px 2px rgba(0,0,0,.25);
  }
  .cta {
    display: flex;
    align-items: center;
    justify-content: center;
    gap: .45em;
    color: var(--white);
    border-radius: 8px;
    background: linear-gradient(180deg, var(--btn-top) 0%, var(--btn-mid) 45%, var(--btn-bottom) 100%);
    box-shadow: 2px 3px 4px rgba(0,0,0,.4);
    letter-spacing: .02em;
  }
  .cta svg { width: .55em; height: .6em; }
  .brand {
    display: flex;
    align-items: center;
    gap: 6px;
    font-family: "Lato", Arial, sans-serif;
    color: var(--ink);
    white-space: nowrap;
  }
  .brand-dot {
    border-radius: 50%;
    border: 2px solid var(--ink);
    background: var(--white);
    flex: none;
  }
  .white-wave { left: 0; bottom: 0; width: 100%; }

  /* 468 x 60 */
  .b-slim { left: 460px; top: 215px; width: 511px; height: 65px; }
  .b-slim .photo-woman { left: 20px; top: -20px; width: 130px; height: 95px; }
  .b-slim .headline-box { left: 161px; top: 0; width: 80px; height: 65px; font-size: 29px; line-height: .95; padding: 5px 4px 0; }
  .b-slim .subline { left: 241px; top: 4px; width: 84px; font-size: 21px; line-height: .88; }
  .b-slim .photo-man { left: 345px; top: 6px; width: 36px; height: 59px; }
  .b-slim .brand { left: 398px; top: 4px; font-size: 11px; }
  .b-slim .brand-dot { width: 20px; height: 20px; }
  .b-slim .cta { left: 389px; top: 32px; width: 110px; height: 26px; font-size: 19px; border-radius: 5px; }

  /* 728 x 90 */
  .b-leader { left: 178px; top: 303px; width: 793px; height: 98px; }
  .b-leader .photo-man.lead { left: 8px; top: 8px; width: 70px; height: 90px; }
  .b-leader .photo-woman { left: 128px; top: -10px; width: 140px; height: 108px; }
  .b-leader .headline-box { left: 273px; top: 0; width: 112px; height: 98px; font-size: 41px; padding: 11px 6px 0; }
  .b-leader .subline { left: 386px; top: 6px; width: 120px; font-size: 31px; }
  .b-leader .photo-man.side { left: 514px; top: 8px; width: 70px; height: 90px; }
  .b-leader .brand { left: 605px; top: 5px; font-size: 18px; }
  .b-leader .brand-dot { width: 34px; height: 34px; }
  .b-leader .cta { left: 603px; top: 52px; width: 157px; height: 37px; font-size: 28px; }

  /* 300 x 250 */
  .b-rect { left: 33px; top: 423px; width: 328px; height: 272px; }
  .b-rect .photo-woman { left: 218px; top: 2px; width: 110px; height: 185px; }
  .b-rect .photo-man { left: 9px; top: 100px; width: 60px; height: 120px; }
  .b-rect .headline-box { left: 52px; top: 5px; font-size: 36px; padding: 4px 4px 0; }
  .b-rect .subline { right: 134px; top: 79px; font-size: 37px; }
  .b-rect .cta { left: 129px; top: 191px; width: 184px; height: 43px; font-size: 31px; }
  .b-rect .brand { left: 11px; top: 228px; font-size: 16px; }
  .b-rect .brand-dot { width: 36px; height: 36px; }

  /* 336 x 280 */
  .b-large { left: 387px; top: 423px; width: 366px; height: 305px; }
  .b-large .photo-woman { left: 223px; top: 2px; width: 142px; height: 228px; }
  .b-large .photo-man { left: 22px; top: 122px; width: 66px; height: 125px; }
  .b-large .headline-box { left: 54px; top: 2px; font-size: 42px; padding: 6px 6px 2px; }
  .b-large .subline { right: 148px; top: 89px; font-size: 41px; }
  .b-large .cta { left: 148px; top: 215px; width: 203px; height: 47px; font-size: 34px; }
  .b-large .brand { left: 16px; top: 253px; font-size: 18px; }
  .b-large .brand-dot { width: 40px; height: 40px; }

  /* 180 x 150 */
  .b-small { left: 775px; top: 423px; width: 196px; height: 163px; }
  .b-small .photo-woman { left: 118px; top: 2px; width: 78px; height: 128px; }
  .b-small .photo-man { left: 5px; top: 87px; width: 28px; height: 50px; }
  .b-small .headline-box { left: 15px; top: 4px; font-size: 21px; padding: 2px 3px 0; }
  .b-small .subline { right: 94px; top: 46px; font-size: 21px; }
  .b-small .cta { left: 64px; top: 111px; width: 120px; height: 27px; font-size: 19px; border-radius: 5px; }
  .b-small .brand { left: 9px; top: 138px; font-size: 10px; gap: 4px; }
  .b-small .brand-dot { width: 20px; height: 20px; }

  /* 160 x 600 */
  .b-sky { left: 996px; top: 74px; width: 175px; height: 654px;
    background: linear-gradient(180deg, var(--sun) 0%, var(--lime) 45%, var(--leaf) 75%); }
  .b-sky .photo-woman { left: 40px; top: 0; width: 120px; height: 237px; }
  .b-sky .headline-box { left: 0; top: 237px; width: 175px; height: 66px; font-size: 36px; padding: 2px 0 0 22px; }
  .b-sky .subline { right: 20px; top: 304px; font-size: 37px; }
  .b-sky .cta { left: 20px; top: 414px; width: 139px; height: 33px; font-size: 26px; }
  .b-sky .photo-man { left: 12px; top: 455px; width: 88px; height: 134px; }
  .b-sky .footer-band { left: 0; top: 589px; width: 175px; height: 65px; background: var(--white); }
  .b-sky .brand { left: 11px; top: 603px; font-size: 17px; }
  .b-sky .brand-dot { width: 40px; height: 40px; }
</style>
</head>
<body>

<svg width="0" height="0" style="position:absolute">
  <defs>
    <symbol id="play" viewBox="0 0 10 12"><path d="M0 0 L10 6 L0 12 Z" fill="#fff"/></symbol>
  </defs>
</svg>

<!-- 468 x 60 -->
<section class="banner b-slim">
  <div class="photo-woman" role="img" aria-label="Woman wearing a blue cause tee"></div>
  <div class="headline-box">DRESS<br>BETTER</div>
  <div class="subline">SO OTHERS<br>CAN LIVE<br>BETTER.</div>
  <div class="photo-man" role="img" aria-label="Man wearing a grey cause tee"></div>
  <div class="brand"><span class="brand-dot"></span>Hope in Hand</div>
  <a class="cta">BUY NOW <svg><use href="#play"/></svg></a>
</section>

<!-- 728 x 90 -->
<section class="banner b-leader">
  <div class="photo-man lead" role="img" aria-label="Man wearing a grey cause tee"></div>
  <div class="photo-woman" role="img" aria-label="Woman wearing a blue cause tee"></div>
  <div class="headline-box">DRESS<br>BETTER</div>
  <div class="subline">SO OTHERS<br>CAN LIVE<br>BETTER.</div>
  <div class="photo-man side" role="img" aria-label="Man wearing a grey cause tee"></div>
  <div class="brand"><span class="brand-dot"></span>Hope in Hand</div>
  <a class="cta">BUY NOW <svg><use href="#play"/></svg></a>
</section>

<!-- 300 x 250 -->
<section class="banner b-rect">
  <div class="photo-woman" role="img" aria-label="Woman wearing a blue cause tee"></div>
  <div class="photo-man" role="img" aria-label="Man wearing a grey cause tee"></div>
  <svg class="white-wave" width="328" height="80" viewBox="0 0 328 80"><path d="M0 20 C90 0 200 20 328 80 L0 80 Z" fill="#fff"/></svg>
  <div class="headline-box">DRESS<br>BETTER</div>
  <div class="subline">SO OTHERS<br>CAN LIVE<br>BETTER.</div>
  <a class="cta">BUY NOW <svg><use href="#play"/></svg></a>
  <div class="brand"><span class="brand-dot"></span>Hope in Hand</div>
</section>

<!-- 336 x 280 -->
<section class="banner b-large">
  <div class="photo-woman" role="img" aria-label="Woman wearing a blue cause tee"></div>
  <div class="photo-man" role="img" aria-label="Man wearing a grey cause tee"></div>
  <svg class="white-wave" width="366" height="80" viewBox="0 0 366 80"><path d="M0 12 C110 -4 230 20 366 80 L0 80 Z" fill="#fff"/></svg>
  <div class="headline-box">DRESS<br>BETTER</div>
  <div class="subline">SO OTHERS<br>CAN LIVE<br>BETTER.</div>
  <a class="cta">BUY NOW <svg><use href="#play"/></svg></a>
  <div class="brand"><span class="brand-dot"></span>Hope in Hand</div>
</section>

<!-- 180 x 150 -->
<section class="banner b-small">
  <div class="photo-woman" role="img" aria-label="Woman wearing a blue cause tee"></div>
  <div class="photo-man" role="img" aria-label="Man wearing a grey cause tee"></div>
  <svg class="white-wave" width="196" height="30" viewBox="0 0 196 30"><path d="M0 4 C60 -2 130 6 196 30 L0 30 Z" fill="#fff"/></svg>
  <div class="headline-box">DRESS<br>BETTER</div>
  <div class="subline">SO OTHERS<br>CAN LIVE<br>BETTER.</div>
  <a class="cta">BUY NOW <svg><use href="#play"/></svg></a>
  <div class="brand"><span class="brand-dot"></span>Hope in Hand</div>
</section>

<!-- 160 x 600 -->
<section class="banner b-sky">
  <div class="photo-woman" role="img" aria-label="Woman wearing a blue cause tee"></div>
  <div class="headline-box">DRESS<br>BETTER</div>
  <div class="subline">SO OTHERS<br>CAN LIVE<br>BETTER.</div>
  <a class="cta">BUY NOW <svg><use href="#play"/></svg></a>
  <div class="photo-man" role="img" aria-label="Man wearing a grey cause tee"></div>
  <div class="footer-band"></div>
  <div class="brand"><span class="brand-dot"></span>Hope in Hand</div>
</section>

</body>
</html>
```